Flyer for the teaching seminar on prayer

I need a creative, but attractive and professional flyer made for an up coming church event.

Here is the content I would like to have on the Flyer:

The name of the event: House of Vigil
Speaker: Bishop Lemuchar Idanwe
Speakers photo: <See attachement>
Date and Time:
Friday March 29th - 7:00 PM to 9:00 PM
Saturday Marche 30th - 7:00 PM to 9:00 PM
Sunday March 31st - 10:00 AM to 12:30 PM
Location:
Falvin Community Center
482 Dunmore Lane, Portland, ME 04117
Welcome to TELVO, where the sky meets the soil.

```html
<!DOCTYPE html>
<html lang="en">
<head>
<meta charset="utf-8">
<title>House of Vigil – Flyer</title>
<link rel="stylesheet" href="https://fonts.googleapis.com/css2?family=Cinzel:wght@600;700&family=EB+Garamond:wght@600&family=Oswald:wght@500&family=Roboto:wght@500;700&display=swap">
<style>
  :root {
    --navy: #063457;
    --orange: #f0931f;
    --orange-deep: #d9801c;
    --white: #ffffff;
    --backdrop: #e4e4e4;
    --photo-dark: #2f3a40;
    --photo-mid: #5b6460;
  }
  * { margin: 0; padding: 0; box-sizing: border-box; }
  html, body {
    width: 1200px; height: 1200px; overflow: hidden;
    background: var(--backdrop);
  }
  .flyer {
    position: absolute; left: 190px; top: 20px;
    width: 974px; height: 1378px;
    transform: scale(0.842); transform-origin: top left;
    overflow: hidden;
    background: var(--navy);
  }
  .event-photo {
    position: absolute; inset: 0;
    background: radial-gradient(ellipse at 70% 35%, var(--photo-mid) 0%, var(--photo-dark) 70%);
  }
  .shapes { position: absolute; inset: 0; }
  .brand {
    position: absolute; left: 40px; top: 500px;
    display: flex; align-items: center; gap: 16px;
  }
  .brand-dot { width: 34px; height: 34px; border-radius: 50%; background: var(--orange); }
  .brand-name {
    font-family: "Cinzel", serif; font-weight: 600;
    font-size: 76px; color: var(--white); letter-spacing: 2px;
  }
  .title-top {
    position: absolute; left: 28px; top: 622px;
    font-family: "Cinzel", serif; font-weight: 700;
    font-size: 68px; color: var(--orange); line-height: 1;
  }
  .title-main {
    position: absolute; left: 26px; top: 690px;
    font-family: "Cinzel", serif; font-weight: 700;
    font-size: 118px; color: var(--white); line-height: 1;
  }
  .speaker-band {
    position: absolute; left: 0; top: 823px; width: 600px; height: 56px;
    background: var(--orange);
    font-family: "Oswald", sans-serif; font-weight: 500;
    font-size: 36px; color: var(--white);
    padding-left: 30px; line-height: 56px;
  }
  .speaker-photo {
    position: absolute; left: 589px; top: 643px;
    width: 330px; height: 330px; border-radius: 50%;
    border: 6px solid var(--orange);
    background: radial-gradient(circle at 50% 40%, #6a7f9e 0%, #3c5678 60%, #4d6a3a 100%);
  }
  .schedule-label {
    position: absolute; left: 25px; top: 913px;
    width: 227px; height: 36px; border-radius: 18px;
    background: var(--white); color: var(--navy);
    font-family: "EB Garamond", serif; font-weight: 600;
    font-size: 28px; line-height: 36px; text-align: center;
  }
  .schedule {
    position: absolute; left: 28px; top: 976px; width: 540px;
    list-style: none;
    font-family: "Oswald", sans-serif; font-weight: 500;
    font-size: 26px; color: var(--white);
  }
  .schedule li { height: 54px; line-height: 42px; border-bottom: 2px dotted var(--orange); }
  .schedule li:last-child { border-bottom: none; }
  .schedule .time { color: var(--orange); }
  .welcome {
    position: absolute; left: 52px; top: 1158px;
    font-family: "Roboto", sans-serif; font-weight: 700;
    font-size: 33px; color: var(--white); line-height: 52px; letter-spacing: 0.5px;
  }
  .venue {
    position: absolute; left: 38px; top: 1288px;
    display: flex; gap: 14px; align-items: flex-start;
    font-family: "Roboto", sans-serif; font-weight: 700;
    font-size: 22px; color: var(--white); line-height: 26px;
  }
</style>
</head>
<body>
  <main class="flyer">
    <div class="event-photo" role="img" aria-label="Blurred photo of a worship gathering with raised hands and a speaker on stage"></div>
    <svg class="shapes" viewBox="0 0 974 1378" aria-hidden="true">
      <polygon points="0,0 580,0 0,403" fill="var(--orange-deep)"/>
      <polygon points="120,0 580,0 0,403 0,250" fill="var(--orange)"/>
      <polygon points="0,403 217,258 797,1378 0,1378" fill="var(--navy)"/>
      <polygon points="974,1033 712,1223 797,1378 974,1378" fill="var(--orange)"/>
      <path d="M40 1183 H30 V1265 H677 L625 1183 H445" fill="none" stroke="var(--orange)" stroke-width="3"/>
    </svg>

    <div class="brand">
      <span class="brand-dot"></span>
      <span class="brand-name">TELVO</span>
    </div>

    <h1 class="title-top">HOUSE OF</h1>
    <h2 class="title-main">VIGIL</h2>

    <div class="speaker-band">Speaker : Bishop Lemuchar Idanwe</div>
    <div class="speaker-photo" role="img" aria-label="Portrait of Bishop Lemuchar Idanwe speaking into a microphone"></div>

    <div class="schedule-label">Date and Time :</div>
    <ul class="schedule">
      <li>Friday March 29th - <span class="time">7:00 PM to 9:00 PM</span></li>
      <li>Saturday March 30th - <span class="time">7:00 PM to 9:00 PM</span></li>
      <li>Sunday March 31st - <span class="time">10:00 AM to 12:30 PM</span></li>
    </ul>

    <p class="welcome">WELCOME TO TELVO<br>WHERE THE SKY MEETS THE SOIL</p>

    <address class="venue">
      <svg width="24" height="34" viewBox="0 0 24 34" aria-hidden="true">
        <path d="M12 0C5.4 0 0 5.2 0 11.7 0 20 12 34 12 34s12-14 12-22.3C24 5.2 18.6 0 12 0z" fill="var(--orange)"/>
        <circle cx="12" cy="11.5" r="4.5" fill="var(--navy)"/>
      </svg>
      <span>Falvin Community Center<br>482 Dunmore Lane, Portland, ME 04117</span>
    </address>
  </main>
</body>
</html>
```